Commercial HVAC and Refrigeration Business cards

Frost-Haven Company is looking for flashy new business cards! We design, install, service and maintain commercial refrigeration, air conditioning, heating and refrigeration equipment. Our colors are blue and white. I'm open to single and double sided designs. Each employee will have their own business card. I've attached a copy of our current logo.

Our website, office and cell phone (cell phone is optional), email address should be clearly legible. "24 Hour Service" and the services we offer are; Sales, Service, Design, Installation, Maintenance. Refrigeration, Heating, Air Conditioning, Ice Machines. Does not have to be in any order.

Target Market(s)

Commercial; Restaurants, hotels, bars, breweries etc.

Industry/Entity Type

Hvac

Contact Information for Business Card

Name; Job Title, Phone Number, Email Address. www.frost-haven-example.com 24 Hour Service. We provide - Sales, Design, Installation, Service, Maintenance. We service - Refrigeration, Heating, Air Conditioning, Ice Machines

Font styles to use
Other font styles liked:
• Be creative

Colors
0255a3
ffffff

Requirements
Must have
• Professional appearance and appeal to commercial clients in the food-service and hospitality industry. Must be clearly legible and easy to understand.
Nice to have
• We want to sell maintenance agreements, perhaps we can use the back of the card to tie into a webpage about our maintenance agreements.
Should not have
• Cartoons or unprofessional. Nothing too edgy.

```html
<!DOCTYPE html>
<html lang="en">
<head>
<meta charset="utf-8">
<title>Frost-Haven Company – Business Cards</title>
<link rel="stylesheet" href="https://fonts.googleapis.com/css2?family=Open+Sans:wght@400;600;700&display=swap">
<style>
  :root {
    --brand-blue: #1c4587;
    --ink-black: #000000;
    --swoosh-grey: #c9c9c9;
    --paper-white: #ffffff;
    --backdrop: #e6e6e6;
    --card-w: 560px;
    --card-h: 320px;
  }
  * { box-sizing: border-box; margin: 0; padding: 0; }
  html, body {
    width: 1200px; height: 900px; overflow: hidden;
    background: var(--backdrop);
    font-family: "Open Sans", sans-serif;
  }
  .canvas { position: relative; width: 1200px; height: 900px; }
  .card {
    position: absolute; left: 320px;
    width: var(--card-w); height: var(--card-h);
    overflow: hidden; color: var(--paper-white);
    box-shadow: 0 2px 6px rgba(0,0,0,.18);
  }
  .card--front { top: 100px; background: var(--brand-blue); }
  .card--back { top: 480px; background: var(--brand-blue); text-align: center; }

  .front-art { position: absolute; inset: 0; width: 100%; height: 100%; }
  .wordmark {
    position: absolute; left: 26px; top: 128px;
    font-size: 21px; font-weight: 600; color: var(--paper-white);
    white-space: nowrap;
  }

  .contact {
    position: absolute; right: 30px; top: 46px;
    text-align: right; line-height: 1.3;
  }
  .contact__name { font-size: 19px; font-weight: 700; }
  .contact__title { font-size: 15px; margin-bottom: 10px; }
  .contact__address { font-size: 15px; margin-bottom: 10px; }
  .contact__line { display: flex; justify-content: flex-end; align-items: center; gap: 8px; font-size: 14.5px; }
  .contact__icon { width: 12px; height: 12px; flex: none; }
  .contact__service { font-size: 20px; font-weight: 700; margin-top: 10px; }

  .back-wordmark {
    margin-top: 64px;
    font-size: 30px; font-weight: 600; color: var(--paper-white);
  }
  .offer { margin-top: 26px; line-height: 1.35; font-size: 16px; }
  .offer__heading { font-weight: 700; }
  .offer + .offer { margin-top: 10px; }
</style>
</head>
<body>
<main class="canvas">

  <section class="card card--front" aria-label="Business card front">
    <svg class="front-art" viewBox="0 0 560 320" preserveAspectRatio="none" aria-hidden="true">
      <path d="M0 0 H255 C300 90 285 230 170 320 H0 Z" fill="var(--ink-black)"/>
      <path d="M255 0 H282 C322 110 295 240 205 320 H170 C285 230 300 90 255 0 Z" fill="var(--swoosh-grey)"/>
      <path d="M282 0 H287 C328 110 300 240 212 320 H205 C295 240 322 110 282 0 Z" fill="var(--paper-white)"/>
    </svg>

    <div class="wordmark">Frost-Haven Company</div>

    <div class="contact">
      <p class="contact__name">Daniel Marsh</p>
      <p class="contact__title">Managing Director</p>
      <p class="contact__address">12345, Address Goes Here<br>Country Name, 123456.</p>
      <p class="contact__line">044-555 010 200
        <svg class="contact__icon" viewBox="0 0 24 24" aria-hidden="true"><path fill="currentColor" d="M6.6 10.8a15 15 0 0 0 6.6 6.6l2.2-2.2a1 1 0 0 1 1-.25 11.4 11.4 0 0 0 3.6.57 1 1 0 0 1 1 1V20a1 1 0 0 1-1 1A17 17 0 0 1 3 4a1 1 0 0 1 1-1h3.5a1 1 0 0 1 1 1c0 1.25.2 2.45.57 3.57a1 1 0 0 1-.25 1z"/></svg>
      </p>
      <p class="contact__line">info@frost-haven-example.com
        <svg class="contact__icon" viewBox="0 0 24 24" aria-hidden="true"><path fill="currentColor" d="M2 5h20v14H2z M4 7v.5l8 5 8-5V7l-8 5z" fill-rule="evenodd"/></svg>
      </p>
      <p class="contact__line">www.frost-haven-example.com
        <svg class="contact__icon" viewBox="0 0 24 24" aria-hidden="true"><circle cx="12" cy="12" r="10" fill="currentColor"/><path d="M2 12h20M12 2c3 3 3 17 0 20M12 2c-3 3-3 17 0 20" stroke="var(--brand-blue)" stroke-width="1.5" fill="none"/></svg>
      </p>
      <p class="contact__service">24 Hour Service</p>
    </div>
  </section>

  <section class="card card--back" aria-label="Business card back">
    <div class="back-wordmark">Frost-Haven Company</div>
    <div class="offer">
      <p class="offer__heading">We provide</p>
      <p>Sales, Design, Installation, Service, Maintenance.</p>
    </div>
    <div class="offer">
      <p class="offer__heading">We service</p>
      <p>Refrigeration, Heating, Air Conditioning, Ice Machines</p>
    </div>
  </section>

</main>
</body>
</html>
```